依頼詳細
----------------------------------『要件』------------------------------------

【 スクリーンショット枚数 】
合計3枚

【 納品サイズ 】
iPhone6:2208(ヨコ) x 1242
iPhoneX:2688(ヨコ) x 1242
iPad Pro12:2732(ヨコ) x 2048

※各サイズ3枚ずつ

ご応募をお待ちしております!
記載項目
【 1枚目テキスト/希望構成 】
タイトル:新しい恋見つけました。
サブタイ:コトラナはあなたの恋の悩みを解決するお手伝いをします。
幸せな恋にこだわる方にオススメです。

・チャットで気軽に本格占い
・24時間いつでも相談OK
・1通目必ず無料

【 2枚目テキスト/希望構成 】
タイトル:最強の占い師軍団が、あなたにとって最高の出逢いを導きます
恋愛、結婚、出産、就職、転職…あなたの人生の分かれ道を占い師がサポートします。

【 3枚目テキスト/希望構成 】
タイトル:機能充実。安心の口コミ機能
レビューをチェックして自分にぴったりの占い師に相談することができます。

【 利用可能なアプリ内画像、及び画像素材 】

本件に添付しております素材をお使いください。
サイズ
• 2208(ヨコ) x 1242
希望イメージ
シンプル 複雑
単色 カラフル
暗い 明るい
日常 高級
遊び心 厳粛
未来的 伝統的
女性的 男性的
希望する色
青系、水色系、紫系
納品ファイル
• イラストレーター形式 (.ai)
• フォトショップ形式 (.psd)
• PNG形式 (.png)
補足説明

最も自分のイメージに印象が近いものでしたので、選定とさせて頂きました。

皆様、ご丁寧に対応を頂き、誠にありがとうございました。

```html
<!DOCTYPE html>
<html lang="ja">
<head>
<meta charset="utf-8">
<title>コトラナ ストア用スクリーンショット</title>
<link href="https://fonts.googleapis.com/css2?family=M+PLUS+Rounded+1c:wght@700;800;900&family=Noto+Sans+JP:wght@500;700;900&family=Dancing+Script:wght@700&display=swap" rel="stylesheet">
<style>
  :root{
    --pink:#e64b8c;
    --pink-deep:#d0336f;
    --pink-soft:#fbd3e5;
    --pink-pale:#fff0f6;
    --purple:#8b3db8;
    --purple-deep:#5e2283;
    --lilac:#e8d3f5;
    --ink:#3b2a3a;
    --white:#ffffff;
    --gold:#f3b63c;
  }
  *{margin:0;padding:0;box-sizing:border-box}
  html,body{width:1200px;height:2236px;overflow:hidden;background:var(--white)}
  body{position:relative;font-family:"Noto Sans JP",sans-serif;color:var(--ink)}
  .shot{position:absolute;left:0;width:1200px;height:700px;overflow:hidden}
  .shot--love{top:0;background:linear-gradient(120deg,#fde4ef 0%,#f9c6dc 55%,#f4b0cf 100%)}
  .shot--masters{top:768px;background:radial-gradient(circle at 40% 35%,#fff6fb 0%,#f8cfe2 55%,#e9a6d2 100%)}
  .shot--reviews{top:1536px;background:radial-gradient(circle at 55% 40%,#fff8fc 0%,#f8d7ea 60%,#e8b3d9 100%)}
  .placeholder{position:absolute}

  /* shot 1 */
  .love-photo{right:0;top:0;width:560px;height:700px;background:linear-gradient(160deg,#f7d6e2 0%,#e8b9c4 45%,#c98f9d 100%)}
  .love-title{position:absolute;left:40px;top:20px;font-family:"M PLUS Rounded 1c",sans-serif;font-weight:900;font-size:168px;line-height:1;color:var(--pink);-webkit-text-stroke:6px var(--white);paint-order:stroke fill;letter-spacing:-4px;white-space:nowrap}
  .love-title__accent{position:absolute;left:400px;top:16px;font-family:"Dancing Script",cursive;font-size:52px;color:var(--pink-deep);letter-spacing:0}
  .love-title__sub{position:absolute;left:330px;top:190px;font-family:"M PLUS Rounded 1c",sans-serif;font-weight:800;font-size:42px;color:var(--pink-deep);letter-spacing:0;-webkit-text-stroke:0}
  .love-lead{position:absolute;left:44px;top:268px;width:640px;font-weight:900;font-size:40px;line-height:1.45;color:var(--pink-deep);text-shadow:0 0 6px var(--white),0 0 6px var(--white);white-space:nowrap}
  .love-points{position:absolute;left:44px;top:420px;display:flex;gap:26px;list-style:none}
  .love-point{width:184px;height:184px;border-radius:50%;background:var(--white);box-shadow:0 6px 16px rgba(208,51,111,.25);display:flex;flex-direction:column;align-items:center;justify-content:center;text-align:center;font-weight:700;font-size:25px;line-height:1.3;color:var(--ink)}
  .love-point svg{width:52px;height:44px;margin-bottom:6px}
  .love-badge{position:absolute;left:870px;top:380px;width:290px;height:290px;border-radius:50%;background:rgba(255,255,255,.88);display:flex;flex-direction:column;align-items:center;justify-content:center;text-align:center;font-family:"M PLUS Rounded 1c",sans-serif;font-weight:800;color:var(--pink-deep)}
  .love-badge__big{font-size:46px;line-height:1.2}
  .love-badge__small{font-size:30px;margin-top:6px}

  /* shot 2 */
  .master{width:190px;height:190px;border-radius:50%;top:40px;border:6px solid var(--white);background:linear-gradient(180deg,#e9d6cf,#b7958b)}
  .master--1{left:60px}.master--2{left:280px}.master--3{left:500px}
  .phone{border-radius:36px;border:10px solid #2a2a2e;background:linear-gradient(180deg,#fff 0%,#eef7f6 100%)}
  .masters-phone{left:800px;top:20px;width:370px;height:720px}
  .masters-title{position:absolute;left:40px;top:280px;font-family:"M PLUS Rounded 1c",sans-serif;font-weight:900;color:var(--purple);-webkit-text-stroke:5px var(--white);paint-order:stroke fill;white-space:nowrap}
  .masters-title__main{font-size:74px;line-height:1.1;letter-spacing:-2px}
  .masters-title__sub{font-size:37px;line-height:1.5;color:var(--purple-deep)}
  .masters-tags{position:absolute;left:50px;top:475px;display:flex;gap:16px;list-style:none}
  .masters-tag{width:128px;height:76px;border-radius:10px;background:var(--purple);color:var(--white);font-weight:900;font-size:38px;display:flex;align-items:center;justify-content:center}
  .masters-band{position:absolute;left:0;top:590px;width:780px;height:66px;background:linear-gradient(90deg,rgba(94,34,131,.85),rgba(139,61,184,.4));color:var(--white);font-weight:700;font-size:28px;display:flex;align-items:center;padding-left:56px;white-space:nowrap}

  /* shot 3 */
  .reviews-phone{left:60px;top:70px;width:390px;height:700px;transform:rotate(-4deg)}
  .reviews-photo{right:0;top:0;width:480px;height:700px;background:linear-gradient(170deg,#fbe6ee 0%,#e9c2c9 50%,#c8959f 100%)}
  .reviews-badges{position:absolute;left:560px;top:60px;display:flex;gap:10px}
  .reviews-badge{width:82px;height:82px;border-radius:12px;background:var(--purple);color:var(--white);font-family:"M PLUS Rounded 1c",sans-serif;font-weight:900;font-size:54px;display:flex;align-items:center;justify-content:center}
  .reviews-title{position:absolute;left:500px;top:160px;font-family:"M PLUS Rounded 1c",sans-serif;font-weight:900;color:var(--pink-deep);-webkit-text-stroke:6px var(--white);paint-order:stroke fill;line-height:1.1;white-space:nowrap}
  .reviews-title__line1{font-size:96px;padding-left:40px}
  .reviews-title__line2{font-size:104px;letter-spacing:-2px}
  .reviews-lead{position:absolute;left:520px;top:420px;width:560px;font-weight:900;font-size:40px;line-height:1.45;color:var(--purple-deep);text-shadow:0 0 6px var(--white),0 0 6px var(--white);white-space:nowrap}
</style>
</head>
<body>

<section class="shot shot--love">
  <div class="placeholder love-photo" role="img" aria-label="スマートフォンを手に微笑む女性の写真"></div>
  <h1 class="love-title">新しい恋<span class="love-title__accent">New love</span><span class="love-title__sub">見つけました。</span></h1>
  <p class="love-lead">コトラナはあなたの恋の悩みを<br>解決するお手伝いをします。</p>
  <ul class="love-points">
    <li class="love-point">
      <svg viewBox="0 0 52 44"><path d="M4 4h44v26H22l-10 10V30H4z" fill="none" stroke="#e64b8c" stroke-width="4" stroke-linejoin="round"/></svg>
      チャットで<br>気軽に<br>本格占い
    </li>
    <li class="love-point">
      <svg viewBox="0 0 52 44"><circle cx="26" cy="22" r="19" fill="none" stroke="#e64b8c" stroke-width="4"/><path d="M26 10v12l8 6" fill="none" stroke="#e64b8c" stroke-width="4" stroke-linecap="round"/></svg>
      24時間<br>いつでも<br>相談OK
    </li>
    <li class="love-point">
      <svg viewBox="0 0 52 44"><rect x="4" y="6" width="44" height="32" rx="3" fill="none" stroke="#e64b8c" stroke-width="4"/><path d="M6 9l20 16 20-16" fill="none" stroke="#e64b8c" stroke-width="4"/></svg>
      1通目<br>必ず無料
    </li>
  </ul>
  <div class="love-badge">
    <span class="love-badge__big">幸せな恋に</span>
    <span class="love-badge__small">こだわる方に<br>オススメです</span>
  </div>
</section>

<section class="shot shot--masters">
  <div class="placeholder master master--1" role="img" aria-label="女性占い師の写真"></div>
  <div class="placeholder master master--2" role="img" aria-label="年配の女性占い師の写真"></div>
  <div class="placeholder master master--3" role="img" aria-label="男性占い師の写真"></div>
  <div class="placeholder phone masters-phone" role="img" aria-label="占い師一覧を表示したアプリ画面"></div>
  <h2 class="masters-title">
    <span class="masters-title__main">最強の占い師軍団が、</span><br>
    <span class="masters-title__sub">あなたにとって最高の出逢いを導きます。</span>
  </h2>
  <ul class="masters-tags">
    <li class="masters-tag">恋愛</li>
    <li class="masters-tag">結婚</li>
    <li class="masters-tag">出産</li>
    <li class="masters-tag">就職</li>
    <li class="masters-tag">転職</li>
  </ul>
  <p class="masters-band">あなたの人生の分かれ道を占い師がサポートします。</p>
</section>

<section class="shot shot--reviews">
  <div class="placeholder reviews-photo" role="img" aria-label="スマートフォンを見る女性の写真"></div>
  <div class="placeholder phone reviews-phone" role="img" aria-label="レビュー一覧を表示したアプリ画面"></div>
  <div class="reviews-badges">
    <span class="reviews-badge">機</span><span class="reviews-badge">能</span><span class="reviews-badge">充</span><span class="reviews-badge">実</span>
  </div>
  <h2 class="reviews-title">
    <span class="reviews-title__line1">安心の</span><br>
    <span class="reviews-title__line2">口コミ機能!</span>
  </h2>
  <p class="reviews-lead">レビューをチェックして<br>自分にぴったりの占い師に<br>相談することができます。</p>
</section>

</body>
</html>
```